Need Bold, Hip Card for Concert Ticket Website Gleaming Passes!

Hi there! I am putting together a business/website that sells event tickets (mostly concerts, but also some sports and theater). Think SeatNook, but much smaller. The site is called Gleaming Passes. I have a new logo (attached, with black/red/white color scheme), and am looking for a modern/cool/original business card design. Note that I am thinking of having the card itself in the shape of a ticket (die cut), so you may want to keep that in mind when designing, but I'm not set on that. I'm also open to alternative card sizes, thicknesses, glossy, spot UV, etc. in order to stand out. I'm attaching a potential die cut template and a sample card using that template in case you want to work with that.
Target Market(s)
Music fans, people that like going to see live events
Industry/Entity Type
Entertainment
Contact Information for Business Card
Information that I'd like to have:
website address - www.gleamingpasses.example
phone number: 1-833-5GLEAMNG (532-6264)
my name - Wendel Pike

```html
<!DOCTYPE html>
<html lang="en">
<head>
<meta charset="utf-8">
<title>Gleaming Passes – Business Card</title>
<link rel="stylesheet" href="https://fonts.googleapis.com/css2?family=Lato:wght@400;700;900&display=swap">
<style>
  :root {
    --backdrop: #ecebe8;
    --card-white: #ffffff;
    --brand-red: #8e0000;
    --ink: #1a1a1a;
    --rule: #cfcfcf;
    --reverse-text: #ffffff;
  }
  html, body {
    margin: 0;
    padding: 0;
    width: 1064px;
    height: 1200px;
    overflow: hidden;
    background: var(--backdrop);
    font-family: "Lato", Arial, sans-serif;
  }
  .canvas {
    position: relative;
    width: 1064px;
    height: 1200px;
  }
  .card {
    position: absolute;
    left: 213px;
    width: 670px;
    height: 414px;
    box-sizing: border-box;
    overflow: hidden;
  }
  .card--front {
    top: 169px;
    background: var(--card-white);
  }
  .card--back {
    top: 631px;
    background: var(--brand-red);
  }

  /* Front */
  .brand {
    position: absolute;
    left: 130px;
    top: 52px;
    display: flex;
    align-items: center;
    gap: 22px;
  }
  .brand__square {
    width: 74px;
    height: 74px;
    background: var(--brand-red);
    flex: none;
  }
  .wordmark {
    margin: 0;
    color: var(--brand-red);
    font-weight: 900;
    line-height: 1;
  }
  .wordmark__top {
    display: block;
    font-size: 56px;
    letter-spacing: 0.5px;
  }
  .wordmark__bottom {
    display: block;
    font-size: 38px;
    letter-spacing: 27px;
    margin-top: 4px;
  }
  .divider {
    position: absolute;
    left: 64px;
    right: 64px;
    top: 221px;
    height: 1px;
    background: var(--rule);
  }
  .person {
    position: absolute;
    left: 68px;
    top: 240px;
  }
  .person__name {
    margin: 0;
    color: var(--brand-red);
    font-weight: 700;
    font-size: 28px;
    line-height: 1.1;
  }
  .person__title {
    margin: 3px 0 0;
    color: var(--ink);
    font-size: 16px;
    letter-spacing: 0.2px;
  }
  .address {
    position: absolute;
    left: 68px;
    top: 313px;
    margin: 0;
    font-style: normal;
    color: var(--ink);
    font-size: 19px;
    line-height: 24.5px;
  }
  .contacts {
    position: absolute;
    right: 62px;
    top: 293px;
    margin: 0;
    padding: 0;
    list-style: none;
    color: var(--ink);
    font-size: 18px;
    line-height: 23px;
  }
  .contacts__item {
    display: flex;
    justify-content: flex-end;
    align-items: center;
    gap: 8px;
  }
  .contacts__icon {
    width: 15px;
    height: 15px;
    fill: var(--brand-red);
    flex: none;
  }

  /* Back */
  .reverse-mark {
    position: absolute;
    left: 113px;
    top: 146px;
    margin: 0;
    color: var(--reverse-text);
    font-weight: 900;
    line-height: 1;
  }
  .reverse-mark__top {
    display: block;
    font-size: 78px;
    letter-spacing: 0.5px;
  }
  .reverse-mark__bottom {
    display: block;
    font-size: 56px;
    letter-spacing: 36px;
    margin-top: 8px;
  }
</style>
</head>
<body>
<main class="canvas">

  <section class="card card--front" aria-label="Business card front">
    <div class="brand">
      <span class="brand__square" aria-hidden="true"></span>
      <h1 class="wordmark">
        <span class="wordmark__top">GLEAMING</span>
        <span class="wordmark__bottom">PASSES</span>
      </h1>
    </div>

    <div class="divider"></div>

    <div class="person">
      <p class="person__name">WENDEL PIKE</p>
      <p class="person__title">MANAGING DIRECTOR</p>
    </div>

    <address class="address">
      88 Marquee Lane, Suite 4,<br>
      Harbor City, 20731<br>
      Stageland
    </address>

    <ul class="contacts">
      <li class="contacts__item">1-833-5GLEAMNG
        <svg class="contacts__icon" viewBox="0 0 16 16" aria-hidden="true"><path d="M1 5c0-2 3-3 7-3s7 1 7 3v1h-3V4.5C11 4 9.5 3.8 8 3.8S5 4 4 4.5V6H1zM4 7h8l2 6H2z"/></svg>
      </li>
      <li class="contacts__item">532-6264
        <svg class="contacts__icon" viewBox="0 0 16 16" aria-hidden="true"><path d="M4 1h8v14H4zM5.5 3v9h5V3zM7.3 13h1.4v1H7.3z" fill-rule="evenodd"/></svg>
      </li>
      <li class="contacts__item">wendel@gleamingpasses.example
        <svg class="contacts__icon" viewBox="0 0 16 16" aria-hidden="true"><path d="M1 3h14v10H1zM2.5 4.5 8 9l5.5-4.5zM2.5 6v5.5h11V6L8 10.5z" fill-rule="evenodd"/></svg>
      </li>
      <li class="contacts__item">www.gleamingpasses.example
        <svg class="contacts__icon" viewBox="0 0 16 16" aria-hidden="true"><circle cx="8" cy="8" r="7"/><path d="M5 4c2 0 2 2 4 2s1 3-1 3-1 3-3 2M10 11c1-1 2 0 3-1" stroke="#fff" stroke-width="1.2" fill="none"/></svg>
      </li>
    </ul>
  </section>

  <section class="card card--back" aria-label="Business card back">
    <p class="reverse-mark">
      <span class="reverse-mark__top">GLEAMING</span>
      <span class="reverse-mark__bottom">PASSES</span>
    </p>
  </section>

</main>
</body>
</html>
```